Its time for a new website

We are at a point now where we are in desperate need of a new website. It was last updated 2006 but still looks like its 1995. We are looking for something eye catching to our clients but easy to navigate and add/remove photos of jobs/trucks and information. Our key business is the manufacture of fire appliances and resale of parts and equipment.

www.korlenrescue.com.au

Coding

Coded - Design and coding required

Number of Pages Required

5+ page

Requirements
Must have
• Logo

```html
<!DOCTYPE html>
<html lang="en">
<head>
<meta charset="utf-8">
<title>Korlen Rescue</title>
<link rel="stylesheet" href="https://fonts.googleapis.com/css2?family=Exo+2:wght@500;600;700&family=Open+Sans:wght@400;600;700&display=swap">
<style>
:root{
  --blue:#0a8fd6;
  --red:#b5151f;
  --red-dark:#8e0f17;
  --ink:#333;
  --muted:#666;
  --dark:#2a2a2a;
  --light:#f0eff0;
  --line:#9a9a9a;
  --white:#fff;
}
*{box-sizing:border-box;margin:0;padding:0}
html,body{width:1200px;height:2769px;overflow:hidden}
body{position:relative;background:var(--white);font-family:"Open Sans",Arial,sans-serif;color:var(--ink)}
.abs{position:absolute}
.topbar{left:0;top:0;width:1200px;height:37px;background:var(--blue)}
.topbar .email{left:790px;top:10px;color:#fff;font-size:13px;display:flex;align-items:center;gap:8px;white-space:nowrap}
.topbar .social{left:1006px;top:9px;display:flex;gap:12px;padding-left:14px;border-left:1px solid rgba(255,255,255,.5)}
.topbar .social span{width:18px;height:18px;border-radius:50%;background:#fff;display:block}
.brand{left:100px;top:6px;display:flex;align-items:center;gap:10px}
.brand .mark{width:60px;height:60px;border-radius:50%;background:var(--red)}
.brand .name{font-family:"Exo 2",sans-serif;font-weight:600;font-size:22px;color:var(--blue);margin-top:40px}
.helpline{left:940px;top:58px;display:flex;align-items:center;gap:10px}
.helpline .ic{width:42px;height:42px;border-radius:50%;background:var(--blue);display:flex;align-items:center;justify-content:center}
.helpline small{display:block;font-size:14px;color:var(--muted)}
.helpline b{font-size:18px;font-weight:400;color:#111}
.nav{left:0;top:124px;width:1200px;height:51px;background:var(--red);border-bottom:3px solid var(--red-dark)}
.nav ul{list-style:none;display:flex;margin-left:100px;height:48px;align-items:center}
.nav li{color:#fff;font-weight:600;font-size:14.5px;padding:0 11px;height:48px;line-height:48px}
.nav li.on{background:var(--red-dark)}
.hero{left:0;top:175px;width:1200px;height:440px;background:linear-gradient(100deg,#5b5650 0%,#c2471b 18%,#7a3a20 30%,#dfe2e6 45%,#eef0f2 65%,#7b7f86 85%,#4a4d52 100%)}
.hero-cap{background:rgba(150,10,20,.88);color:#fff;font-family:"Exo 2",sans-serif;font-weight:600;font-size:29px;line-height:38px;padding:8px 30px;white-space:nowrap}
.dots{left:566px;top:580px;display:flex;gap:10px}
.dots i{width:14px;height:14px;border-radius:50%;background:#fff;display:block}
.dots i:first-child{background:var(--red)}
.ticker{left:0;top:615px;width:1200px;height:86px;background:var(--blue);color:#fff;font-size:18px;display:flex;align-items:center;justify-content:center}
.ticker svg{position:absolute;top:29px}
.sec-title{height:46px;line-height:46px;color:#fff;background:var(--dark);font-family:"Exo 2",sans-serif;font-weight:700;font-size:20px;text-align:center;transform:skewX(-14deg);box-shadow:5px 5px 0 var(--red)}
.sec-title span{display:inline-block;transform:skewX(14deg)}
.intro{left:230px;top:818px;width:740px;text-align:center;font-size:13px;line-height:26px;color:var(--muted)}
.card{width:308px;height:347px;border:2px solid var(--line);background:var(--light)}
.card .photo{position:absolute;left:0;top:0;width:304px;height:210px;border-radius:0 0 50% 50%/0 0 34% 34%}
.card .hex{position:absolute;left:122px;top:190px}
.card h3{position:absolute;left:0;right:0;top:278px;text-align:center;font-family:"Exo 2",sans-serif;font-weight:600;font-size:27px;color:var(--red)}
.news{width:308px}
.news .photo{height:177px;border:2px solid var(--line)}
.news .meta{display:flex;gap:10px;margin-top:8px}
.news h4{color:var(--red);font-size:13.5px;font-weight:700;text-transform:uppercase}
.news .posted{font-size:12px;color:var(--muted);margin-top:7px;display:flex;align-items:center;gap:6px}
.news p{font-size:12.5px;line-height:21px;color:var(--muted);text-align:justify;margin-top:4px}
.news .more{position:absolute;top:340px;right:0;color:var(--red);font-size:13px;display:flex;align-items:center;gap:6px}
.news .more.boxed{border:1.5px solid var(--red);padding:1px 0 1px 8px}
.news .more.boxed em{background:var(--red);padding:0 8px;display:flex}
.fband{left:0;top:2238px;width:1200px;height:84px;background:var(--dark)}
.fband .grey{position:absolute;left:0;top:0;width:420px;height:84px;background:#d9d9d9;clip-path:polygon(0 0,380px 0,420px 84px,0 84px)}
.fband .fname{left:118px;top:46px;color:var(--blue);font-family:"Exo 2",sans-serif;font-weight:600;font-size:13px}
.fband .fname i{width:28px;height:28px;border-radius:50%;background:var(--red);display:block;position:absolute;left:22px;top:-32px}
.fband .emerg{right:220px;top:28px;color:#fff;font-family:"Exo 2",sans-serif;font-weight:700;font-size:20px}
.fband .social{right:100px;top:31px;display:flex;gap:10px}
.fband .social span{width:20px;height:20px;border-radius:50%;background:#fff;display:block}
.map{left:0;top:2322px;width:1200px;height:383px;background:linear-gradient(135deg,#e4e4e4,#d6d6d6 50%,#e2e2e2)}
.addr{left:436px;top:2494px;width:216px;height:60px;background:#fff;border:1px solid #999;font-size:13px;text-align:center;padding-top:8px;line-height:21px;color:#222}
.cbtn{top:2567px;width:56px;height:56px;display:flex;align-items:center;justify-content:center;background:#fff;border:1px solid #bbb}
.cbtn.on{background:var(--blue);border-color:var(--blue)}
.bottom{left:0;top:2705px;width:1200px;height:64px;background:var(--dark);color:#fff;font-size:12px}
.bottom .copy{left:88px;top:24px}
.bottom .links{right:90px;top:24px;display:flex;gap:9px}
</style>
</head>
<body>

<div class="abs topbar">
  <div class="abs email">
    <svg width="18" height="13" viewBox="0 0 18 13"><rect x="1" y="1" width="16" height="11" fill="none" stroke="#fff" stroke-width="1.5"/><path d="M1 1l8 6 8-6" fill="none" stroke="#fff" stroke-width="1.5"/></svg>
    info@korlenrescue.com.au
  </div>
  <div class="abs social"><span></span><span></span><span></span></div>
</div>

<div class="abs brand"><div class="mark"></div><div class="name">Korlen Rescue</div></div>

<div class="abs helpline">
  <div class="ic"><svg width="22" height="22" viewBox="0 0 24 24"><path d="M6 2l4 4-2 3c1 3 4 6 7 7l3-2 4 4-3 4C10 21 3 14 2 5z" fill="#fff"/></svg></div>
  <div><small>custom helpline</small><b>08 5550 1742</b></div>
</div>

<nav class="abs nav"><ul>
  <li class="on">Home</li><li>About Us</li><li>Pumpers</li><li>Tankers</li><li>GPA/Rescue</li><li>Light Tankers</li><li>Trailers</li><li>Slip-on Units</li><li>NEW for 2006</li><li>Contact Us</li>
</ul></nav>

<div class="abs hero" role="img" aria-label="Fire engine driving past a burning truck"></div>
<div class="abs hero-cap" style="left:110px;top:442px">Western Australia's Largest, most experienced</div>
<div class="abs hero-cap" style="left:212px;top:498px">competent manufacturer of fire fighting vehicles</div>
<div class="abs dots"><i></i><i></i><i></i></div>

<div class="abs ticker">
  <svg style="left:30px" width="16" height="28" viewBox="0 0 16 28"><path d="M14 2L2 14l12 12" fill="none" stroke="#fff" stroke-width="2"/></svg>
  Lorem ipsum dolor sit amet, consecte adipiscing elit. Suspendisse condimentum porttitor cursumus. Duis&nbsp; nec nulla turpis.
  <svg style="right:30px" width="16" height="28" viewBox="0 0 16 28"><path d="M2 2l12 12L2 26" fill="none" stroke="#fff" stroke-width="2"/></svg>
</div>

<div class="abs sec-title" style="left:396px;top:758px;width:316px"><span>CHECK OUT OUR SERVICE</span></div>
<p class="abs intro">Lorem ipsum dolor sit amet, consecte adipiscing elit. Suspendisse condimentum porttitor cursumus. Duis<br>nec nulla turpis. Nulla lacinia laoreet odio</p>

<svg width="0" height="0" style="position:absolute"><defs>
<symbol id="hex" viewBox="0 0 60 64"><path d="M30 2l26 15v30L30 62 4 47V17z" fill="var(--red)" stroke="#fff" stroke-width="3"/><path d="M21 40v-7c0-4 3-6 7-6h8v-5l8 8-8 8v-5h-7c-3 0-5 1-5 4z" fill="none" stroke="#fff" stroke-width="2"/></symbol>
<symbol id="hexd" viewBox="0 0 60 64"><path d="M30 2l26 15v30L30 62 4 47V17z" fill="#222" stroke="#fff" stroke-width="3"/><path d="M21 40v-7c0-4 3-6 7-6h8v-5l8 8-8 8v-5h-7c-3 0-5 1-5 4z" fill="none" stroke="#fff" stroke-width="2"/></symbol>
</defs></svg>

<div class="abs card" style="left:100px;top:901px"><div class="photo" role="img" aria-label="Red pumper fire truck" style="background:linear-gradient(160deg,#cfd8d4,#b8242a 55%,#7d8a6a)"></div><svg class="hex" width="60" height="64"><use href="#hex"/></svg><h3>Pumpers</h3></div>
<div class="abs card" style="left:447px;top:901px"><div class="photo" role="img" aria-label="Stainless steel water tanker truck" style="background:linear-gradient(160deg,#5d6670,#8a8f96 50%,#44494f)"></div><svg class="hex" width="60" height="64"><use href="#hexd"/></svg><h3>Tankers</h3></div>
<div class="abs card" style="left:794px;top:901px"><div class="photo" role="img" aria-label="General purpose rescue truck at fire station" style="background:linear-gradient(160deg,#d8d8d8,#c32a2e 55%,#8a8a7a)"></div><svg class="hex" width="60" height="64"><use href="#hex"/></svg><h3>GPA/Rescue</h3></div>
<div class="abs card" style="left:100px;top:1285px"><div class="photo" role="img" aria-label="Light tanker utility truck in a garage" style="background:linear-gradient(160deg,#8a6a4a,#d9d6d0 45%,#b22a2a 70%,#777)"></div><svg class="hex" width="60" height="64"><use href="#hex"/></svg><h3>Light Tankers</h3></div>
<div class="abs card" style="left:447px;top:1285px"><div class="photo" role="img" aria-label="Trailer with red water tank and hose reel" style="background:linear-gradient(160deg,#a69a7a,#d8403a 50%,#8a8272)"></div><svg class="hex" width="60" height="64"><use href="#hex"/></svg><h3>Trailers</h3></div>
<div class="abs card" style="left:794px;top:1285px"><div class="photo" role="img" aria-label="Yellow slip-on pump unit" style="background:linear-gradient(160deg,#6a7a8a,#e2b51a 50%,#7a6a4a)"></div><svg class="hex" width="60" height="64"><use href="#hex"/></svg><h3>Slip-on Units</h3></div>

<div class="abs sec-title" style="left:456px;top:1703px;width:258px"><span>LATEST NEWS</span></div>

<svg width="0" height="0" style="position:absolute"><defs>
<symbol id="clock" viewBox="0 0 14 14"><circle cx="7" cy="7" r="6" fill="none" stroke="#999" stroke-width="1.3"/><path d="M7 3v4h3" fill="none" stroke="#999" stroke-width="1.3"/></symbol>
<symbol id="arr" viewBox="0 0 14 10"><path d="M0 5h12M8 1l4 4-4 4" fill="none" stroke="currentColor" stroke-width="1.3"/></symbol>
</defs></svg>

<div class="abs news" style="left:100px;top:1780px;height:370px">
  <div class="photo" role="img" aria-label="Firefighters in yellow helmets beside a fire engine" style="background:linear-gradient(120deg,#3a2a22,#c99a1a 40%,#6a2a22 70%,#b52a22)"></div>
  <div class="meta">
    <svg width="50" height="54" viewBox="0 0 60 64"><path d="M30 2l26 15v30L30 62 4 47V17z" fill="var(--red)"/><text x="30" y="30" font-size="13" fill="#fff" text-anchor="middle" font-family="Open Sans,sans-serif">28</text><text x="30" y="45" font-size="13" fill="#fff" text-anchor="middle" font-family="Open Sans,sans-serif">May</text></svg>
    <div><h4>Morbi non sem a lacus porta</h4><div class="posted"><svg width="14" height="14"><use href="#clock"/></svg>POSTED&nbsp; 29 MAY 2015</div></div>
  </div>
  <p>Lorem ipsum dolor sit amet, scelerata nunc intuens munus oblitus ait regem orem ipsum</p>
  <div class="more">Read more <svg width="14" height="10"><use href="#arr"/></svg></div>
</div>

<div class="abs news" style="left:447px;top:1780px;height:370px">
  <div class="photo" role="img" aria-label="Aerial ladder fire trucks parked on a lot" style="background:linear-gradient(160deg,#9fb3c6,#d0d3d4 40%,#c2302a 70%,#5a6a4a)"></div>
  <div class="meta">
    <svg width="50" height="54" viewBox="0 0 60 64"><path d="M30 2l26 15v30L30 62 4 47V17z" fill="var(--red)"/><text x="30" y="30" font-size="13" fill="#fff" text-anchor="middle" font-family="Open Sans,sans-serif">24</text><text x="30" y="45" font-size="13" fill="#fff" text-anchor="middle" font-family="Open Sans,sans-serif">May</text></svg>
    <div><h4>Morbi non sem</h4><div class="posted"><svg width="14" height="14"><use href="#clock"/></svg>POSTED&nbsp; 29 MAY 2015</div></div>
  </div>
  <p>Lorem ipsum dolor sit amet, scelerata nunc intuens munus oblitus ait regem orem ipsum dolor sit amet, scelerata nunc [...]</p>
  <div class="more boxed">Read more <em><svg width="14" height="10" style="color:#fff"><use href="#arr"/></svg></em></div>
</div>

<div class="abs news" style="left:794px;top:1780px;height:370px">
  <div class="photo" role="img" aria-label="Two firefighters standing in front of a red fire engine" style="background:linear-gradient(160deg,#c9ccc8,#c2302a 45%,#6a6a5a 80%)"></div>
  <div class="meta">
    <svg width="50" height="54" viewBox="0 0 60 64"><path d="M30 2l26 15v30L30 62 4 47V17z" fill="var(--red)"/><text x="30" y="30" font-size="13" fill="#fff" text-anchor="middle" font-family="Open Sans,sans-serif">20</text><text x="30" y="45" font-size="13" fill="#fff" text-anchor="middle" font-family="Open Sans,sans-serif">May</text></svg>
    <div><h4>Morbi non sem a lacus porta</h4><div class="posted"><svg width="14" height="14"><use href="#clock"/></svg>POSTED&nbsp; 29 MAY 2015</div></div>
  </div>
  <p>Lorem ipsum dolor sit amet, scelerata nunc intuens munus oblitus ait regem</p>
  <div class="more">Read more <svg width="14" height="10"><use href="#arr"/></svg></div>
</div>

<div class="abs fband">
  <div class="grey"></div>
  <div class="abs fname"><i></i>Korlen Rescue</div>
  <div class="abs emerg">24/7 Emergency Service: 1-800-555-0142</div>
  <div class="abs social"><span></span><span></span><span></span></div>
</div>

<div class="abs map" role="img" aria-label="Street map of the workshop location"></div>
<svg class="abs" style="left:716px;top:2352px" width="44" height="58" viewBox="0 0 44 58"><path d="M22 2C11 2 3 10 3 21c0 14 19 35 19 35s19-21 19-35C41 10 33 2 22 2z" fill="#777"/><circle cx="22" cy="21" r="7" fill="#ddd"/></svg>
<div class="abs addr">Lot 14 Harlow Road<br>Brenton 6399 Western Australia</div>
<div class="abs cbtn on" style="left:513px"><svg width="24" height="32" viewBox="0 0 24 32"><path d="M12 2C6 2 2 6 2 12c0 8 10 18 10 18s10-10 10-18C22 6 18 2 12 2z" fill="none" stroke="#fff" stroke-width="2"/><circle cx="12" cy="12" r="3.5" fill="none" stroke="#fff" stroke-width="2"/></svg></div>
<div class="abs cbtn" style="left:578px"><svg width="32" height="22" viewBox="0 0 32 22"><rect x="1" y="1" width="30" height="20" fill="none" stroke="#333" stroke-width="2"/><path d="M1 1l15 11L31 1M1 21l11-10M31 21L20 11" fill="none" stroke="#333" stroke-width="2"/></svg></div>
<div class="abs cbtn" style="left:643px"><svg width="30" height="30" viewBox="0 0 24 24"><path d="M6 2l4 4-2 3c1 3 4 6 7 7l3-2 4 4-3 4C10 21 3 14 2 5z" fill="none" stroke="#333" stroke-width="1.6"/></svg></div>

<footer class="abs bottom">
  <div class="abs copy">Korlen Rescue© 2015. Privacy Policy</div>
  <div class="abs links"><span>Home</span><span>About Us</span><span>Pumpers</span><span>Tankers</span><span>GPA/Rescue</span><span>Light Tankers</span><span>Trailers</span><span>Slip-on Units</span><span>Contact Us</span></div>
</footer>

</body>
</html>
```